Bright Orchard
Bright & Fun-filled
Talia Brennick
Certified Holistic Wellness Coach, NLP Practitioner
no address pls
talia@brightorchard.com
www.brightorchard.com
To love oneself is the beginning of a lifelong romance. --Edwin Tarrow

```html
<!DOCTYPE html>
<html lang="en">
<head>
<meta charset="utf-8">
<title>Bright Orchard — Business Cards</title>
<link rel="stylesheet" href="https://fonts.googleapis.com/css2?family=Arimo:wght@400;700&display=swap">
<style>
  :root {
    --backdrop: #ece8e3;
    --card-white: #ffffff;
    --card-shade: #ececee;
    --pink: #ea1a5c;
    --pink-deep: #d9124f;
    --ink: #4a4a4f;
    --ink-soft: #6d6d72;
    --rule: #b9b9be;
  }
  * { margin: 0; padding: 0; box-sizing: border-box; }
  html, body { width: 1200px; height: 756px; overflow: hidden; }
  body {
    background: var(--backdrop);
    font-family: "Arimo", Arial, sans-serif;
    position: relative;
  }
  .card {
    position: absolute;
    width: 490px;
    height: 280px;
    border-radius: 14px;
    overflow: hidden;
    box-shadow: 0 6px 18px rgba(0,0,0,0.18);
  }
  .card--front { left: 96px; top: 120px; background: linear-gradient(180deg, var(--card-white) 0%, var(--card-shade) 100%); }
  .card--back { left: 614px; top: 120px; background: var(--pink); }
  .card--plain { left: 355px; top: 448px; background: linear-gradient(180deg, var(--card-white) 0%, var(--card-shade) 100%); }

  .wordmark {
    font-weight: 400;
    font-size: 44px;
    letter-spacing: -0.5px;
    display: flex;
    align-items: center;
    gap: 10px;
    white-space: nowrap;
  }
  .wordmark__dot { width: 14px; height: 14px; border-radius: 50%; flex: none; }

  .card--front .wordmark { position: absolute; left: 34px; top: 52px; color: var(--ink); font-size: 40px; }
  .card--front .wordmark__dot { background: var(--pink); }

  .holder { position: absolute; left: 0; top: 152px; width: 250px; text-align: right; }
  .holder__name { color: var(--pink); font-weight: 700; font-size: 17px; margin-bottom: 5px; }
  .holder__title { color: var(--ink-soft); font-size: 11px; line-height: 1.45; }
  .divider { position: absolute; left: 264px; top: 152px; width: 1px; height: 48px; background: var(--rule); }
  .contact { position: absolute; left: 278px; top: 162px; color: var(--ink-soft); font-size: 11px; line-height: 1.55; }

  .front-rule { position: absolute; left: 0; right: 0; top: 222px; height: 2px; background: var(--pink); }
  .front-band {
    position: absolute; left: 0; right: 0; bottom: 0; height: 50px;
    background: var(--pink);
    color: #fff; font-size: 12px; letter-spacing: 1.5px;
    display: flex; align-items: center; justify-content: center;
  }

  .motif {
    position: absolute; left: 50%; top: 50%;
    width: 260px; height: 230px;
    transform: translate(-50%, -50%);
    border-radius: 50%;
  }
  .card--back .motif { background: radial-gradient(closest-side, rgba(255,255,255,0.12), rgba(255,255,255,0)); }
  .card--plain .motif { background: radial-gradient(closest-side, rgba(234,26,92,0.08), rgba(234,26,92,0)); }

  .card--back .wordmark,
  .card--plain .wordmark {
    position: absolute; left: 50%; top: 50%;
    transform: translate(-50%, -50%);
  }
  .card--back .wordmark { color: #fff; }
  .card--back .wordmark__dot { background: #fff; }
  .card--plain .wordmark { color: var(--ink); }
  .card--plain .wordmark__dot { background: var(--pink); }
</style>
</head>
<body>
  <section class="card card--front" aria-label="Business card front">
    <div class="wordmark"><span>Bright Orchard</span><span class="wordmark__dot"></span></div>
    <div class="holder">
      <p class="holder__name">Talia Brennick</p>
      <p class="holder__title">Certified Holistic Wellness Coach<br>NLP Practitioner</p>
    </div>
    <div class="divider"></div>
    <div class="contact">
      <p>Cell: 555.014.2280</p>
      <p>talia@brightorchard.com</p>
    </div>
    <div class="front-rule"></div>
    <div class="front-band">www.brightorchard.com</div>
  </section>

  <section class="card card--back" aria-label="Business card back">
    <div class="motif" role="img" aria-label="Faint brand motif decoration"></div>
    <div class="wordmark"><span>Bright Orchard</span><span class="wordmark__dot"></span></div>
  </section>

  <section class="card card--plain" aria-label="Business card alternate back">
    <div class="motif" role="img" aria-label="Faint brand motif decoration"></div>
    <div class="wordmark"><span>Bright Orchard</span><span class="wordmark__dot"></span></div>
  </section>
</body>
</html>
```